IT Services company general flyer

Looking for a printable US letter size flyer to give a brief overview of the services we offer. We also partner with another company for their services as well. Please check out our website at www.gizmobykellan.com and click on "Our Services" to learn about our services and visit www.bluefernguard,com and click on services to learn about their services. Several of our services do overlap, so they only need to be on the flyer once. Let me know if this is too much content and we need to weed some out. We do not want Home phone service on this flyer. The basic design of the flyer should mimic similar to the VOIP one you did for me for the colors and logo. Also check out the "Who Choose us" page on www.gizmobykellan.com to include some of that as well.

Target Market(s)

Targeting Small businesses that may not normally have a budget for their IT Services

Industry/Entity Type

It Service

Font styles to use
Serif
Sans Serif

Requirements
Must have
• Must include my logo, phone number and email/website address and must follow the same basic template of my previous flyers.

```html
<!DOCTYPE html>
<html lang="en">
<head>
<meta charset="utf-8">
<title>Gizmo by Kellan – Our Services</title>
<link href="https://fonts.googleapis.com/css2?family=Hind:wght@400;600;700&family=Oswald:wght@400;500;700&display=swap" rel="stylesheet">
<style>
  :root {
    --navy: #1b2849;
    --navy-deep: #17223f;
    --red: #b5221e;
    --white: #ffffff;
    --offwhite: #ececec;
    --rule: #c9cfdc;
  }
  * { margin: 0; padding: 0; box-sizing: border-box; }
  html, body { width: 849px; height: 1200px; overflow: hidden; background: var(--white); }
  .flyer { position: relative; width: 849px; height: 1200px; overflow: hidden; font-family: "Hind", sans-serif; }

  .brand-panel { position: absolute; left: 0; top: 0; width: 386px; height: 188px; background: var(--white); }
  .brand { position: absolute; left: 52px; top: 52px; display: flex; align-items: center; gap: 18px; }
  .brand-mark { width: 64px; height: 64px; background: var(--red); }
  .brand-name { font-family: "Hind", sans-serif; font-weight: 700; color: var(--navy); font-size: 38px; line-height: 0.95; }
  .brand-name span { display: block; }

  .hero-photo { position: absolute; left: 0; top: 188px; width: 386px; height: 780px;
    background: radial-gradient(ellipse at 58% 30%, #d9eefc 0%, #5d9ad8 12%, #2c4f86 32%, #1c2c4d 60%, #141c2f 100%); }

  .services { position: absolute; left: 386px; top: 0; width: 463px; height: 968px; background: var(--navy); color: var(--white); }
  .services-title { position: absolute; left: 57px; top: 50px; font-family: "Oswald", sans-serif; font-weight: 500; font-size: 36px; letter-spacing: 0.5px; line-height: 1; }
  .service { position: absolute; left: 124px; width: 270px; }
  .service h3 { font-family: "Hind", sans-serif; font-weight: 700; font-size: 19.5px; line-height: 1.1; margin-bottom: 1px; }
  .service p { font-size: 17px; line-height: 20.5px; font-weight: 400; }
  .service-rule { position: absolute; left: 124px; width: 257px; height: 1px; background: var(--rule); }
  .service-icon { position: absolute; left: 63px; width: 48px; height: 48px; }

  .contact-band { position: absolute; left: 0; top: 968px; width: 849px; height: 171px; background: var(--red); }
  .phone-icon { position: absolute; left: 128px; top: 995px; width: 80px; height: 80px; }
  .phone-number { position: absolute; left: 228px; top: 982px; font-family: "Oswald", sans-serif; font-weight: 700; font-size: 92px; line-height: 1; color: var(--offwhite); letter-spacing: -1px; }
  .mail-icon { position: absolute; left: 254px; top: 1081px; width: 35px; height: 27px; }
  .email { position: absolute; left: 312px; top: 1078px; font-family: "Oswald", sans-serif; font-weight: 400; font-size: 27px; line-height: 1; color: var(--offwhite); }

  .social-tab { position: absolute; left: 2px; top: 1109px; width: 218px; height: 30px; background: var(--navy);
    clip-path: polygon(0 0, 88% 0, 100% 100%, 0 100%); }
  .social-tab span { position: absolute; left: 35px; top: 8px; color: var(--white); font-size: 12.5px; font-weight: 400; letter-spacing: 0.2px; }
  .social-tab i { position: absolute; left: 112px; top: 6px; width: 16px; height: 16px; background: var(--white); border-radius: 3px; }

  .web-band { position: absolute; left: 0; top: 1139px; width: 849px; height: 61px; background: var(--navy); }
  .website { position: absolute; left: 0; width: 849px; top: 1147px; text-align: center; font-family: "Oswald", sans-serif; font-size: 35px; color: var(--white); line-height: 1; padding-left: 4px; }
</style>
</head>
<body>
<div class="flyer">
  <header class="brand-panel">
    <div class="brand">
      <div class="brand-mark"></div>
      <div class="brand-name"><span>GIZMO</span><span>BY KELLAN</span></div>
    </div>
  </header>

  <div class="hero-photo" role="img" aria-label="Photo of a businessman's hand touching a glowing digital interface with technology graphics"></div>

  <section class="services">
    <h2 class="services-title">OUR SERVICES</h2>

    <svg class="service-icon" style="top:172px" viewBox="0 0 48 48" fill="none" stroke="#fff" stroke-width="2.4">
      <rect x="14" y="4" width="18" height="20" rx="2"/><line x1="14" y1="11" x2="32" y2="11"/><line x1="14" y1="17" x2="32" y2="17"/>
      <path d="M10 40 a7 7 0 0 1 2-13 a9 9 0 0 1 17-2 a7 7 0 0 1 9 8 a5 5 0 0 1-2 7z" fill="#fff"/>
      <line x1="4" y1="22" x2="4" y2="36"/><line x1="44" y1="14" x2="44" y2="30"/>
    </svg>
    <div class="service" style="top:139px">
      <h3>Managed IT Service</h3>
      <p>You need your IT systems for your day to day work. Let us help manage and protect them.</p>
    </div>
    <div class="service-rule" style="top:230px"></div>

    <svg class="service-icon" style="top:342px" viewBox="0 0 48 48" fill="#fff">
      <circle cx="24" cy="15" r="10"/><path d="M6 46 a18 14 0 0 1 36 0z"/>
      <path d="M13 15 a11 11 0 0 1 22 0" fill="none" stroke="#fff" stroke-width="2.5"/>
    </svg>
    <div class="service" style="top:295px">
      <h3>Business VOIP Phone Service</h3>
      <p>Reduce cost and improve commu-<br>nication for your business. Solutions available for any size business from 1 phone to hundreds of phones.</p>
    </div>
    <div class="service-rule" style="top:410px"></div>

    <svg class="service-icon" style="top:515px" viewBox="0 0 48 48" fill="none" stroke="#fff" stroke-width="2.4">
      <rect x="4" y="14" width="18" height="16" rx="2" fill="#fff"/><path d="M8 14 v-5 a5 5 0 0 1 10 0 v5"/>
      <circle cx="30" cy="26" r="11"/><line x1="19" y1="26" x2="41" y2="26"/><ellipse cx="30" cy="26" rx="5" ry="11"/>
      <circle cx="40" cy="10" r="5"/><circle cx="24" cy="42" r="5"/><line x1="4" y1="42" x2="18" y2="42" stroke-dasharray="2 2"/>
    </svg>
    <div class="service" style="top:477px">
      <h3>Network Security</h3>
      <p>Worried about the latest ransom-<br>ware or crypto virus? We can help design and protect your network.</p>
    </div>
    <div class="service-rule" style="top:569px"></div>

    <svg class="service-icon" style="top:692px" viewBox="0 0 48 48" fill="none" stroke="#fff" stroke-width="4.5" stroke-linecap="round">
      <path d="M3 18 a30 30 0 0 1 42 0"/><path d="M10 26 a20 20 0 0 1 28 0"/><path d="M17 33 a10 10 0 0 1 14 0"/>
      <circle cx="24" cy="42" r="3.5" fill="#fff" stroke="none"/>
    </svg>
    <div class="service" style="top:637px">
      <h3>Wireless Solutions</h3>
      <p>Is your wireless coverage spotty or would you like to extend your network or internet coverage to another building?</p>
    </div>
    <div class="service-rule" style="top:750px"></div>

    <svg class="service-icon" style="top:846px" viewBox="0 0 48 48" fill="#fff" stroke="#fff" stroke-width="2.4">
      <path d="M9 24 a8 8 0 0 1 3-15 a10 10 0 0 1 19-2 a8 8 0 0 1 9 10 a6 6 0 0 1-3 7z"/>
      <line x1="24" y1="20" x2="24" y2="34"/><line x1="10" y1="30" x2="38" y2="30" fill="none"/>
      <circle cx="9" cy="38" r="6" fill="none"/><circle cx="39" cy="38" r="6" fill="none"/>
    </svg>
    <div class="service" style="top:797px">
      <h3>Cloud Services</h3>
      <p>Want your own business email service? Want to move to the cloud for secure file storage and sharing? Ask us about our complete cloud</p>
    </div>
  </section>

  <footer>
    <div class="contact-band"></div>
    <svg class="phone-icon" viewBox="0 0 80 80" fill="none" stroke="#fff" stroke-width="5">
      <path d="M62 70 A36 36 0 1 1 72 30"/>
      <path d="M24 22 l8-4 6 12-5 4 a24 24 0 0 0 12 12 l4-5 12 6-4 8 c-20 2-34-13-33-33z" fill="#fff" stroke="none"/>
      <path d="M46 20 a16 16 0 0 1 14 14" stroke-width="3.5"/><path d="M46 28 a8 8 0 0 1 6 6" stroke-width="3.5"/>
    </svg>
    <div class="phone-number">555.318.0472</div>
    <svg class="mail-icon" viewBox="0 0 35 27"><rect width="35" height="27" rx="3" fill="#fff"/><path d="M2 4 l15.5 12 15.5-12" fill="none" stroke="#b5221e" stroke-width="3"/></svg>
    <div class="email">sales@gizmobykellan.com</div>
    <div class="social-tab"><span>VISIT US AT</span><i></i></div>
    <div class="web-band"></div>
    <div class="website">www.gizmobykellan.com</div>
  </footer>
</div>
</body>
</html>
```